Start up business website

IT Support provider that caters towards law enforcement / police departments. We'll offer remote IT support, backup / recovery services and cyber security. Will add updates soon.

Target Market(s)

Police departments / Law Enforcement

Coding

Coded - Design and coding required

Number of Pages Required

5+ page

Font styles to use
Other font styles liked:
• Use font style in uploaded logo

Colors
0054AA
0677BA
7BADD7
CADEEF
E8F1F8

```html
<!DOCTYPE html>
<html lang="en">
<head>
<meta charset="utf-8">
<title>Bastion Support Services — Home</title>
<link href="https://fonts.googleapis.com/css2?family=Orbitron:wght@600;800&family=Roboto+Condensed:wght@300;400;700&display=swap" rel="stylesheet">
<style>
:root{
  --blue:#0054AA;
  --blue-mid:#0677BA;
  --sky:#7BADD7;
  --pale:#CADEEF;
  --mist:#E8F1F8;
  --navy:#0d2a66;
  --ink:#111418;
  --grey:#5b6068;
  --footer:#1c1f23;
  --white:#ffffff;
}
*{margin:0;padding:0;box-sizing:border-box}
html,body{width:1200px;height:1200px;overflow:hidden;background:var(--white)}
.stage{position:absolute;left:0;top:0;width:1920px;height:1920px;transform:scale(.625);transform-origin:0 0;font-family:"Roboto Condensed",Arial,sans-serif;color:var(--ink)}
.abs{position:absolute}
.display{font-family:"Orbitron",Arial,sans-serif;font-weight:800;text-transform:uppercase;line-height:1;letter-spacing:.3px}
.accent{color:var(--blue)}
.body-copy{font-size:4.6px;line-height:8px;color:var(--grey);font-weight:300}
.btn{position:absolute;font-family:"Orbitron",Arial,sans-serif;font-weight:600;font-size:3.6px;letter-spacing:.3px;text-transform:uppercase;display:flex;align-items:center;justify-content:center}
.btn-solid{background:var(--blue);color:var(--white)}
.btn-outline{border:1px solid var(--blue);color:var(--blue);background:var(--white)}
.btn-white{background:var(--white);color:var(--blue)}
.photo{position:absolute}

/* header */
.brand{left:812px;top:58px;display:flex;align-items:center;gap:4px;font-family:"Orbitron",Arial,sans-serif;font-weight:800;font-size:8px;color:var(--blue)}
.brand-mark{width:14px;height:14px;background:var(--navy)}
.nav{left:915px;top:64px;display:flex;gap:10px;font-family:"Orbitron",Arial,sans-serif;font-weight:600;font-size:3.6px;text-transform:uppercase}
.nav .is-active{color:var(--blue)}
.nav-underline{left:915px;top:83px;width:14px;height:1px;background:var(--blue)}

/* hero */
.hero{left:750px;top:84px;width:432px;height:203px;overflow:hidden;background:linear-gradient(180deg,#fbfbfc,#f1f2f4)}
.hero-title-1{left:808px;top:136px;font-size:13px}
.hero-title-2{left:808px;top:152px;font-size:20px}
.hero-title-3{left:808px;top:176px;font-size:12.5px}
.hero-copy{left:808px;top:194px;width:150px;font-size:6px;line-height:9px;color:var(--ink)}
.hero-dots{left:959px;top:267px;display:flex;gap:2px}
.hero-dots span{width:4px;height:2px;background:var(--sky)}
.hero-dots .on{background:var(--blue)}

/* about */
.about-bar{left:957px;top:327px;width:5px;height:81px;background:var(--blue)}
.about-title{left:988px;top:336px;font-size:10.5px;line-height:13px}
.about-copy{left:988px;top:380px;width:135px}
.checklist{left:988px;top:422px;list-style:none;font-size:4.6px;color:var(--grey);font-weight:300}
.checklist li{display:flex;align-items:center;gap:3px;height:12.3px}

/* services */
.services-title{left:812px;top:572px;font-size:11px;line-height:13px}
.services-copy{left:812px;top:600px;width:140px}
.service-card{position:absolute;width:73px;height:98px;padding:13px 6px 0;color:var(--white);background:var(--navy);overflow:hidden}
.service-card.is-featured{background:var(--blue)}
.service-card .icon{width:15px;height:15px;margin-bottom:5px}
.service-card h3{font-family:"Orbitron",Arial,sans-serif;font-weight:800;font-size:5px;line-height:7px;text-transform:uppercase;letter-spacing:.3px}
.service-card p{font-size:3.6px;line-height:6.3px;margin-top:4px;font-weight:300;opacity:.9}
.service-card .more{font-family:"Orbitron",Arial,sans-serif;font-size:3px;font-weight:600;margin-top:7px;text-transform:uppercase}
.service-card .corner{position:absolute;right:-6px;bottom:-6px;width:24px;height:24px;border:1px solid rgba(255,255,255,.18);border-radius:50%}
.services-note{left:988px;top:684px;font-size:4.6px;color:var(--grey)}

/* solutions */
.solutions-side{left:757px;top:784px;width:44px;height:179px;background:var(--sky)}
.solutions-photo{left:806px;top:784px;width:369px;height:179px;background:linear-gradient(120deg,#16253b 0%,#2a3a52 45%,#1a2534 100%)}
.solutions-title{left:838px;top:823px;font-size:10.5px;line-height:13px;color:var(--white)}
.solutions-copy{left:838px;top:851px;width:160px;color:#d5dbe4}
.watch{left:1058px;top:827px;width:28px;height:28px;border-radius:50%;background:var(--white);display:flex;align-items:center;justify-content:center}
.watch-label{left:1057px;top:859px;font-size:5px;font-style:italic;color:#d5dbe4}
.stat{position:absolute;top:913px;width:71px;height:50px;padding:10px 0 0 8px}
.stat b{display:block;font-family:"Orbitron",Arial,sans-serif;font-weight:800;font-size:9px;letter-spacing:.3px}
.stat span{display:block;font-size:4.6px;line-height:7px;margin-top:3px}
.stat svg{position:absolute;right:6px;top:12px}
.stat-dark{left:906px;background:rgba(10,18,30,.75);color:var(--white)}
.stat-blue{left:977px;background:var(--blue-mid);color:var(--white)}
.stat-light{left:1048px;background:var(--mist);color:var(--ink)}

/* portfolio / reviews headings */
.section-title{left:750px;width:432px;text-align:center;font-size:11px}
.section-copy{left:870px;width:192px;text-align:center}

/* cjis */
.cjis-band{left:750px;top:1302px;width:325px;height:166px;background:var(--blue)}
.cjis-frame{left:965px;top:1314px;width:80px;height:170px;background:var(--sky)}
.cjis-title{left:812px;top:1330px;font-size:10.5px;line-height:13px;color:var(--white)}
.cjis-copy{left:812px;width:142px;color:#e4edf8}

/* reviews */
.review{position:absolute;top:1561px;width:150px;height:59px;border:1px solid #9aa0a8;padding:8px 8px 0;font-size:4.4px;line-height:8px;color:var(--grey);font-weight:300;background:var(--white)}
.review::before{content:"\201C";position:absolute;left:6px;top:-2px;font-size:22px;color:var(--pale);font-family:Georgia,serif}
.review-tail{position:absolute;width:8px;height:8px;background:var(--white);border-right:1px solid #9aa0a8;border-bottom:1px solid #9aa0a8;transform:rotate(45deg)}
.reviewer{position:absolute;top:1637px;text-align:right;width:80px}
.reviewer b{display:block;font-size:4.6px}
.reviewer span{display:block;font-size:3.6px;color:var(--grey)}
.avatar{position:absolute;top:1631px;width:25px;height:24px;background:linear-gradient(160deg,#c6d4e6,#3b4f6e)}

/* cta & footer */
.footer{left:750px;top:1716px;width:432px;height:166px;background:var(--footer)}
.cta{left:812px;top:1692px;width:312px;height:54px;background:var(--blue)}
.cta-title{left:829px;top:1709px;font-size:7px;line-height:11px;color:var(--white)}
.footer-brand{left:812px;top:1798px;font-family:"Orbitron",Arial,sans-serif;font-weight:800;font-size:7px;color:var(--white);display:flex;flex-direction:column;align-items:center;gap:4px}
.footer-brand i{width:14px;height:14px;background:var(--sky);display:block}
.footer-col{position:absolute;top:1774px;color:#e6e8eb}
.footer-col h4{font-family:"Orbitron",Arial,sans-serif;font-weight:800;font-size:4.6px;text-transform:uppercase;margin-bottom:6px;letter-spacing:.3px}
.footer-col h4 em{font-style:normal;color:var(--sky)}
.footer-col li{list-style:none;font-size:3.8px;line-height:9.2px}
.footer-col .label{color:var(--sky)}
.footer-rule{left:750px;top:1858px;width:432px;height:1px;background:#343940}
.copyright{left:750px;top:1863px;width:432px;text-align:center;font-size:3.8px;color:#c9cdd2}
.copyright em{font-style:normal;color:var(--sky)}
</style>
</head>
<body>
<div class="stage">

  <!-- Header -->
  <div class="abs brand"><span class="brand-mark"></span>BASTION</div>
  <nav class="abs nav">
    <span class="is-active">Home</span><span>Services</span><span>About us</span><span>Follow up</span><span>CJIS compliance</span><span>Contact us</span>
  </nav>
  <div class="abs nav-underline"></div>

  <!-- Hero -->
  <section class="abs hero" role="img" aria-label="Faint flag texture behind the hero text">
    <svg width="432" height="203" viewBox="0 0 432 203">
      <defs>
        <linearGradient id="officerTone" x1="0" y1="0" x2="1" y2="1">
          <stop offset="0" stop-color="#6f7782"/>
          <stop offset=".55" stop-color="#2a2f38"/>
          <stop offset="1" stop-color="#9aa4b2"/>
        </linearGradient>
      </defs>
      <path d="M190 0 C228 20 232 80 252 120 C272 155 330 150 380 168 C405 178 422 190 432 203 L432 0 Z" fill="url(#officerTone)" role="img" aria-label="Photo of a police officer speaking into a shoulder radio"/>
      <path d="M188 0 C226 20 230 80 250 120 C270 157 328 152 378 170 C403 180 420 192 430 203" fill="none" stroke="var(--blue)" stroke-width="5"/>
    </svg>
  </section>
  <h1 class="abs display hero-title-1">Your life</h1>
  <div class="abs display hero-title-2 accent">Is under</div>
  <div class="abs display hero-title-3">Our security</div>
  <p class="abs hero-copy">Strategies focused on increase ingenue private privacy and visibility of your business.</p>
  <a class="btn btn-solid" style="left:808px;top:224px;width:51px;height:14px">Contact us</a>
  <div class="abs hero-dots"><span></span><span class="on"></span><span></span></div>

  <!-- About -->
  <div class="photo" style="left:812px;top:327px;width:128px;height:162px;background:linear-gradient(150deg,#2c4d7c,#0f2340 60%,#49627f)" role="img" aria-label="Photo of support agents wearing headsets at monitors"></div>
  <div class="photo" style="left:854px;top:430px;width:108px;height:81px;background:linear-gradient(135deg,#0b1522,#183a4a 55%,#7a2d2d);border:2px solid var(--white)" role="img" aria-label="Photo of hands on a laptop with a glowing lock icon"></div>
  <div class="abs about-bar"></div>
  <h2 class="abs display about-title">We provide<br>Best <span class="accent">security</span><br><span class="accent">in your city</span></h2>
  <p class="abs body-copy about-copy">We keep police networks running around the clock with remote help, secure backups and steady monitoring. Our team knows the rules your agency must follow and builds support plans that fit your budget, your staff and your daily shifts.</p>
  <ul class="abs checklist">
    <li><svg width="6" height="6" viewBox="0 0 6 6"><path d="M.5 3.2 2.3 5 5.5 1" fill="none" stroke="var(--blue)" stroke-width="1"/></svg>Around the clock help desk for every shift.</li>
    <li><svg width="6" height="6" viewBox="0 0 6 6"><path d="M.5 3.2 2.3 5 5.5 1" fill="none" stroke="var(--blue)" stroke-width="1"/></svg>Encrypted backups kept off site.</li>
    <li><svg width="6" height="6" viewBox="0 0 6 6"><path d="M.5 3.2 2.3 5 5.5 1" fill="none" stroke="var(--blue)" stroke-width="1"/></svg>Threat monitoring across every device and account.</li>
    <li><svg width="6" height="6" viewBox="0 0 6 6"><path d="M.5 3.2 2.3 5 5.5 1" fill="none" stroke="var(--blue)" stroke-width="1"/></svg>Clear reports your chief can read quickly.</li>
  </ul>
  <a class="btn btn-outline" style="left:988px;top:481px;width:43px;height:12px">Learn more</a>

  <!-- Services -->
  <h2 class="abs display services-title">Our<br><span class="accent">Services</span></h2>
  <p class="abs body-copy services-copy">Four focused services built for law enforcement agencies, from help desk to full recovery.</p>

  <article class="service-card is-featured" style="left:969px;top:564px">
    <svg class="icon" viewBox="0 0 16 16" fill="none" stroke="#fff" stroke-width=".8"><circle cx="8" cy="8" r="4"/><path d="M8 1v3M8 12v3M1 8h3M12 8h3M3 3l2 2M11 11l2 2M13 3l-2 2M5 11l-2 2"/></svg>
    <h3>Cyber<br>security</h3>
    <p>Firewalls, monitoring and quick response to keep case files and systems safe.</p>
    <div class="more">Read more</div><span class="corner"></span>
  </article>
  <article class="service-card" style="left:1048px;top:564px">
    <svg class="icon" viewBox="0 0 16 16" fill="none" stroke="#fff" stroke-width=".8"><rect x="2" y="9" width="12" height="5"/><path d="M5 9V6a3 3 0 0 1 6 0v3"/><path d="M4 11.5h2"/></svg>
    <h3>Backup<br>services</h3>
    <p>Daily encrypted copies of records, stored off site and tested each month.</p>
    <div class="more">Read more</div><span class="corner"></span>
  </article>
  <article class="service-card" style="left:812px;top:636px">
    <svg class="icon" viewBox="0 0 16 16" fill="none" stroke="#fff" stroke-width=".8"><circle cx="8" cy="6" r="4"/><path d="M3 15c0-3 2-5 5-5s5 2 5 5"/><path d="M4 6h-1M13 6h-1"/></svg>
    <h3>IT<br>support</h3>
    <p>Remote help desk for officers and staff on every shift of the week.</p>
    <div class="more">Read more</div><span class="corner"></span>
  </article>
  <article class="service-card" style="left:890px;top:636px">
    <svg class="icon" viewBox="0 0 16 16" fill="none" stroke="#fff" stroke-width=".8"><rect x="2" y="3" width="12" height="8"/><path d="M5 14h6M8 11v3M6 7l2-2 2 2"/></svg>
    <h3>Recovery<br>service</h3>
    <p>Fast restore of servers, files and mail after outages or attacks.</p>
    <div class="more">Read more</div><span class="corner"></span>
  </article>
  <p class="abs services-note">You want to check all services click this button now.</p>
  <a class="btn btn-outline" style="left:988px;top:697px;width:49px;height:12px">More services</a>

  <!-- Solutions -->
  <div class="abs solutions-side"></div>
  <div class="abs solutions-photo" role="img" aria-label="Photo of a security operations room with staff at monitors"></div>
  <h2 class="abs display solutions-title">Your<br>simple solutions</h2>
  <p class="abs body-copy solutions-copy">One partner for support, backup and security so your team can stay focused on keeping the city safe.</p>
  <div class="abs watch"><svg width="9" height="10" viewBox="0 0 9 10"><path d="M1 0 9 5 1 10Z" fill="var(--blue-mid)"/></svg></div>
  <div class="abs watch-label">Watch Video</div>
  <div class="stat stat-dark"><b>200+</b><span>Happy<br>Customers</span>
    <svg width="16" height="16" viewBox="0 0 16 16" fill="none" stroke="#fff" stroke-width=".8"><circle cx="5" cy="5" r="2.5"/><circle cx="11" cy="5" r="2.5"/><path d="M1 14c0-3 2-5 4-5s4 2 4 5M7 14c0-3 2-5 4-5s4 2 4 5"/></svg></div>
  <div class="stat stat-blue"><b>150+</b><span>Succeeded<br>Projects</span>
    <svg width="16" height="16" viewBox="0 0 16 16" fill="none" stroke="#fff" stroke-width=".8"><rect x="1.5" y="2.5" width="13" height="11"/><path d="M4 6h8M4 9h5M4 12h6"/></svg></div>
  <div class="stat stat-light"><b>1500+</b><span>Working Hours<br>Were Spent</span>
    <svg width="16" height="16" viewBox="0 0 16 16" fill="none" stroke="var(--ink)" stroke-width=".8"><circle cx="8" cy="8" r="6.5"/><path d="M8 4v4l3 2"/></svg></div>

  <!-- Portfolio -->
  <h2 class="abs display section-title" style="top:997px">Our <span class="accent">Portfolio</span></h2>
  <p class="abs body-copy section-copy" style="top:1010px">A look at recent projects for departments of every size across the region and the state.</p>
  <div class="photo" style="left:812px;top:1042px;width:175px;height:115px;background:linear-gradient(135deg,#1d4f86,#0f2a4a 55%,#4d86b8)" role="img" aria-label="Photo of analysts in a control room with a world map screen"></div>
  <div class="photo" style="left:992px;top:1064px;width:101px;height:93px;background:linear-gradient(135deg,#111,#3a3d44 60%,#1a1c20)" role="img" aria-label="Photo of a hand touching a glowing shield icon"></div>
  <div class="photo" style="left:838px;top:1161px;width:44px;height:54px;background:linear-gradient(135deg,#0f1d33,#3b5a80)" role="img" aria-label="Photo of a digital shield graphic"></div>
  <div class="photo" style="left:887px;top:1161px;width:74px;height:91px;background:linear-gradient(135deg,#0a1f45,#1d6fb0 60%,#0b1a33)" role="img" aria-label="Photo of a laptop with a lock symbol"></div>
  <div class="photo" style="left:966px;top:1161px;width:74px;height:91px;background:linear-gradient(135deg,#0d1d2e,#2d5b78 55%,#a04a7a)" role="img" aria-label="Photo of a fingerprint scan above a laptop"></div>
  <div class="photo" style="left:1045px;top:1161px;width:74px;height:91px;background:linear-gradient(135deg,#5d6470,#1b2330 60%,#8793a3)" role="img" aria-label="Photo of two police officers standing"></div>

  <!-- CJIS -->
  <div class="abs cjis-band"></div>
  <div class="abs cjis-frame"></div>
  <div class="photo" style="left:969px;top:1317px;width:153px;height:165px;background:linear-gradient(135deg,#d7b27a,#6c7f96 50%,#223247)" role="img" aria-label="Photo of hands on a laptop with floating document icons"></div>
  <h2 class="abs display cjis-title">CJIS<br>Compliance</h2>
  <p class="abs body-copy cjis-copy" style="top:1360px">We follow the CJIS Security Policy in every step, from access control to audit logs, so your data stays protected and your agency stays ready for review.</p>
  <p class="abs body-copy cjis-copy" style="top:1390px">Our staff pass background checks and training, and we document each control with clear reports you can share with auditors, city leaders and partner agencies when asked.</p>
  <a class="btn btn-white" style="left:812px;top:1433px;width:43px;height:11px">Learn more</a>

  <!-- Reviews -->
  <h2 class="abs display section-title" style="top:1519px">Customer <span class="accent">Review</span></h2>
  <p class="abs body-copy section-copy" style="top:1532px">What chiefs and IT leads say about working with our support team every day.</p>
  <blockquote class="review" style="left:812px">"Their help desk answers fast, even on night shifts. Since we moved our backups to them we have not lost a single file, and our audit went smoothly with their reports ready."</blockquote>
  <span class="review-tail" style="left:926px;top:1616px"></span>
  <blockquote class="review" style="left:970px">"They handled our move to new servers without downtime. Our officers get help in minutes, and our network has been safer and calmer ever since we signed on."</blockquote>
  <span class="review-tail" style="left:1084px;top:1616px"></span>
  <div class="reviewer" style="left:853px"><b>MARLA QUINN</b><span>Business Man</span></div>
  <div class="avatar" style="left:937px" role="img" aria-label="Portrait of the reviewer"></div>
  <div class="reviewer" style="left:1011px"><b>MARLA QUINN</b><span>Ceo</span></div>
  <div class="avatar" style="left:1095px" role="img" aria-label="Portrait of the reviewer"></div>

  <!-- CTA & Footer -->
  <footer class="abs footer" role="img" aria-label="Faint flag texture across the footer"></footer>
  <div class="abs cta"></div>
  <h2 class="abs display cta-title">We are ready to bring bigger &amp;<br>stronger security services</h2>
  <a class="btn btn-white" style="left:1053px;top:1714px;width:51px;height:13px">Contact us</a>

  <div class="abs footer-brand"><i></i>BASTION</div>
  <div class="footer-col" style="left:897px">
    <h4>Quick <em>links</em></h4>
    <ul><li>Home</li><li>Services</li><li>About us</li><li>Follow up</li><li>CJIS Compliance</li><li>Contact us</li></ul>
  </div>
  <div class="footer-col" style="left:980px">
    <h4>Our <em>services</em></h4>
    <ul><li>IT Support</li><li>Backup Services</li><li>Recovery Services</li><li>Cyber Security</li></ul>
  </div>
  <div class="footer-col" style="left:1067px">
    <h4>Contact <em>us</em></h4>
    <ul><li class="label">Location :</li><li style="line-height:5px">120 Harbor Way, Suite 4</li><li class="label">Phone :</li><li style="line-height:5px">(555) 014 2290</li><li class="label">Email :</li><li style="line-height:5px">hello@bastionsupport.example</li></ul>
  </div>
  <div class="abs footer-rule"></div>
  <p class="abs copyright">Copyright © 2021 <em>Bastion Support Services</em> . All rights reserved.</p>

</div>
</body>
</html>
```